Brasko Construction Business Card

I need a business card design for my company.
We are a construction/machinery company.
I would like to see my logo on the front of the card and my details on the other side
I would like the card to be black or dark grey in colour,with my logo as i send it or modified with a lighter blue colour
I would like to see the design kept fairly simple,but eye catching at the same time
Industry/Entity Type
Business
Contact Information for Business Card
Name
Phone Number
Address
Email
Colors
00a990
1b1b1b
000000
474747
ececec

```html
<!DOCTYPE html>
<html lang="en">
<head>
<meta charset="utf-8">
<title>Brasko Construction Business Card</title>
<link rel="stylesheet" href="https://fonts.googleapis.com/css2?family=Cinzel:wght@400&family=Open+Sans:wght@400;700&display=swap">
<style>
  :root {
    --teal: #15ab96;
    --black: #000000;
    --dark-grey: #1b1b1b;
    --mid-grey: #474747;
    --light: #ececec;
    --white: #ffffff;
    --frame: #bdbdbd;
  }
  * { box-sizing: border-box; margin: 0; padding: 0; }
  html, body {
    width: 1200px;
    height: 1000px;
    overflow: hidden;
    background: var(--white);
  }
  .sheet { position: relative; width: 1200px; height: 1000px; }

  .card-frame {
    position: absolute;
    left: 269px;
    width: 721px;
    height: 433px;
    border: 1px solid var(--frame);
    background: var(--white);
  }
  .card-frame--front { top: 51px; }
  .card-frame--back { top: 500px; }

  .card {
    position: absolute;
    left: 30px;
    background: var(--black);
    width: 660px;
  }
  .card-frame--front .card { top: 17px; height: 398px; }
  .card-frame--back .card { top: 22px; height: 387px; }

  .brand-name {
    position: absolute;
    left: 0;
    right: 0;
    text-align: center;
    font-family: "Open Sans", sans-serif;
    font-weight: 700;
    color: var(--teal);
    text-transform: uppercase;
    line-height: 1;
  }
  .brand-name--front { top: 120px; }
  .brand-name--front .brand-line-main { display: block; font-size: 104px; letter-spacing: 2px; }
  .brand-name--front .brand-line-sub { display: block; font-size: 52px; letter-spacing: 4px; margin-top: 14px; }

  .brand-name--back { top: 55px; }
  .brand-name--back .brand-line-main { display: block; font-size: 44px; letter-spacing: 1px; }
  .brand-name--back .brand-line-sub { display: block; font-size: 22px; letter-spacing: 3px; margin-top: 8px; }

  .person-name {
    position: absolute;
    left: 117px;
    top: 196px;
    font-family: "Cinzel", serif;
    font-size: 32px;
    letter-spacing: 12px;
    color: var(--white);
  }

  .mobile {
    position: absolute;
    left: 395px;
    top: 203px;
    display: flex;
    align-items: center;
    gap: 10px;
  }
  .mobile-badge {
    width: 28px;
    height: 28px;
    background: var(--dark-grey);
  }
  .mobile-number {
    font-family: "Open Sans", sans-serif;
    font-size: 16px;
    color: var(--white);
  }

  .contact-group {
    position: absolute;
    top: 272px;
    font-family: "Open Sans", sans-serif;
    font-size: 15px;
    line-height: 1;
    color: var(--white);
  }
  .contact-group--phone { left: 50px; }
  .contact-group--mail { left: 290px; }
  .contact-group--web { left: 494px; }

  .icon { display: block; fill: var(--white); margin-bottom: 18px; }
  .icon--phone { width: 22px; height: 22px; }
  .icon--mail { width: 23px; height: 18px; margin-top: 2px; margin-bottom: 20px; }
  .icon--web { width: 23px; height: 17px; margin-top: 3px; margin-bottom: 20px; }

  .contact-line { white-space: nowrap; }
  .contact-line + .contact-line { margin-top: 14px; }
  .contact-label { display: inline-block; width: 34px; }
</style>
</head>
<body>
<main class="sheet">

  <section class="card-frame card-frame--front" aria-label="Card front">
    <div class="card">
      <h1 class="brand-name brand-name--front">
        <span class="brand-line-main">Brasko</span>
        <span class="brand-line-sub">Construction</span>
      </h1>
    </div>
  </section>

  <section class="card-frame card-frame--back" aria-label="Card back">
    <div class="card">
      <p class="brand-name brand-name--back">
        <span class="brand-line-main">Brasko</span>
        <span class="brand-line-sub">Construction</span>
      </p>

      <p class="person-name">NAME</p>

      <div class="mobile">
        <div class="mobile-badge">
          <svg viewBox="0 0 28 28" width="28" height="28" aria-hidden="true">
            <g transform="rotate(20 14 14)">
              <rect x="9" y="5" width="10" height="18" rx="2" fill="none" stroke="#ffffff" stroke-width="1.5"/>
              <g fill="#ffffff">
                <rect x="11" y="8" width="1.6" height="1.6"/><rect x="13.2" y="8" width="1.6" height="1.6"/><rect x="15.4" y="8" width="1.6" height="1.6"/>
                <rect x="11" y="10.4" width="1.6" height="1.6"/><rect x="13.2" y="10.4" width="1.6" height="1.6"/><rect x="15.4" y="10.4" width="1.6" height="1.6"/>
                <rect x="11" y="12.8" width="1.6" height="1.6"/><rect x="13.2" y="12.8" width="1.6" height="1.6"/><rect x="15.4" y="12.8" width="1.6" height="1.6"/>
                <rect x="11" y="15.2" width="1.6" height="1.6"/><rect x="13.2" y="15.2" width="1.6" height="1.6"/><rect x="15.4" y="15.2" width="1.6" height="1.6"/>
                <circle cx="14" cy="20" r="1"/>
              </g>
            </g>
          </svg>
        </div>
        <span class="mobile-number">0412 345 678</span>
      </div>

      <div class="contact-group contact-group--phone">
        <svg class="icon icon--phone" viewBox="0 0 24 24" aria-hidden="true">
          <path d="M6.6 10.8c1.4 2.8 3.8 5.2 6.6 6.6l2.2-2.2c.3-.3.7-.4 1-.2 1.1.4 2.3.6 3.6.6.6 0 1 .4 1 1V20c0 .6-.4 1-1 1C10.6 21 3 13.4 3 4c0-.6.4-1 1-1h3.5c.6 0 1 .4 1 1 0 1.3.2 2.5.6 3.6.1.3 0 .7-.2 1l-2.3 2.2z"/>
        </svg>
        <p class="contact-line"><span class="contact-label">tel.</span>07 3123 4567</p>
        <p class="contact-line"><span class="contact-label">fax</span>07 3123 4568</p>
      </div>

      <div class="contact-group contact-group--mail">
        <svg class="icon icon--mail" viewBox="0 0 23 18" aria-hidden="true">
          <path d="M2 0h19a2 2 0 0 1 2 2v1L11.5 10 0 3V2a2 2 0 0 1 2-2z"/>
          <path d="M0 5.3l11.5 7 11.5-7V16a2 2 0 0 1-2 2H2a2 2 0 0 1-2-2z"/>
        </svg>
        <p class="contact-line">info@brasko.com.au</p>
      </div>

      <div class="contact-group contact-group--web">
        <svg class="icon icon--web" viewBox="0 0 24 18" aria-hidden="true">
          <path d="M12 3C7.6 3 3.7 4.7 1 7.5l1.6 1.6C4.9 6.7 8.3 5.2 12 5.2s7.1 1.5 9.4 3.9L23 7.5C20.3 4.7 16.4 3 12 3z"/>
          <path d="M12 7.5c-3 0-5.6 1.2-7.5 3.1l1.6 1.6c1.5-1.5 3.6-2.5 5.9-2.5s4.4 1 5.9 2.5l1.6-1.6C17.6 8.7 15 7.5 12 7.5z"/>
          <path d="M12 12c-1.6 0-3.1.7-4.2 1.8l1.6 1.6c.7-.7 1.6-1.1 2.6-1.1s1.9.4 2.6 1.1l1.6-1.6C15.1 12.7 13.6 12 12 12z"/>
          <circle cx="12" cy="17" r="1.3"/>
        </svg>
        <p class="contact-line">www.brasko.com.au</p>
      </div>
    </div>
  </section>

</main>
</body>
</html>
```